Talbix Pens needs a new Webpage for their collection of ballpens

We at Talbix pens need a brand new webpage to represent our company and range of products. We need a product based website to focus purely on our collection. The web design must bring about a perception of high quality International brand but still affordable in price. Since there are only 5 products, they must all feature on the cover page itself.

Target Market(s)

Stationary Wholesale and retail

Industry/Entity Type

It Company

Number of Pages Required

1 page

Requirements
Must have
• pls see www.quendora-example.com to derive inspiration
Should not have
• stock images
• abstract images
• random pen images

```html
<!DOCTYPE html>
<html lang="en">
<head>
<meta charset="utf-8">
<title>Talbix Pens</title>
<link href="https://fonts.googleapis.com/css2?family=Open+Sans:ital,wght@0,400;0,600;0,700;1,400&family=Roboto+Condensed:wght@400;700&display=swap" rel="stylesheet">
<style>
:root{
  --blue:#1a64a6;
  --blue-band:#2e6fa8;
  --topbar:#1a5f9e;
  --ink:#2d2d2d;
  --muted:#555;
  --page:#f2f2f2;
  --review-bg:#f4f4f4;
  --footer:#264f77;
  --bottom:#2b2b2b;
  --star:#f0a823;
  --swatch-red:#e23a5a;
}
*{margin:0;padding:0;box-sizing:border-box}
html,body{width:1200px;height:2179px;overflow:hidden}
body{position:relative;background:var(--page);font-family:"Open Sans",sans-serif;color:var(--ink)}
.abs{position:absolute}
.topbar{left:0;top:0;width:1200px;height:29px;background:var(--topbar)}
.topbar span{position:absolute;top:8px;font-size:10px;color:#fff;letter-spacing:.2px}
.header{left:0;top:29px;width:1200px;height:93px;background:#fff;border-bottom:1px solid #e3e3e3}
.logo{font-family:"Open Sans",sans-serif;font-weight:700;letter-spacing:4px;color:var(--blue)}
.header-logo{left:97px;top:22px;font-size:36px}
.nav a{position:absolute;top:41px;font-size:13px;color:var(--ink);text-decoration:none;font-family:"Open Sans",sans-serif}
.nav .active{border:1px dashed #444;padding:8px 11px;top:33px}
.framed{border:1px solid #555;outline:1px dashed #888;outline-offset:-6px;display:flex;align-items:center;justify-content:center;font-family:"Roboto Condensed",sans-serif;font-weight:700;color:var(--blue)}
.hero-title{left:145px;top:237px;width:262px;height:51px;font-size:34px}
.hero-text{left:142px;top:307px;width:460px;font-size:12.5px;line-height:21px;color:var(--muted)}
.specs{list-style:none}
.specs li{display:flex;align-items:center;gap:9px;height:30px;font-size:15px;color:var(--ink)}
.specs svg{flex:none}
.hero-specs{left:146px;top:354px}
.swatch{display:inline-block;width:13px;height:13px;border:1px solid #333;margin-left:4px;vertical-align:-2px}
.sw-blue{background:var(--blue)}
.sw-black{background:#111}
.sw-red{background:var(--swatch-red)}
.dots{left:148px;top:467px;display:flex;gap:3px}
.dots i{width:15px;height:15px;border:1px solid #1a64a6;border-radius:50%;display:block}
.dots i.on{background:var(--blue)}
.pen-art{border-radius:6px;background:linear-gradient(135deg,rgba(112,170,222,.35),rgba(230,236,244,.2))}
.pen-purple{background:linear-gradient(160deg,rgba(80,50,160,.3),rgba(220,225,235,.25))}
.welcome-title{left:0;width:1200px;top:652px;text-align:center;font-family:"Roboto Condensed",sans-serif;font-weight:700;font-size:39px;color:#fff;letter-spacing:-.5px}
.welcome-text{left:200px;width:800px;top:712px;text-align:center;font-size:11.5px;line-height:21px;color:#fff}
.products-title{left:459px;top:901px;width:262px;height:52px;font-size:31px}
.product{width:200px}
.product h3{font-family:"Open Sans",sans-serif;font-size:13px;font-weight:400;color:var(--ink)}
.product h3 b{font-weight:700;letter-spacing:2px;margin-right:4px}
.product .specs{margin-top:9px}
.product .specs li{height:27px;font-size:13.5px;gap:6px}
.arrow{width:28px;height:28px;border:1px solid var(--blue);border-radius:50%;display:flex;align-items:center;justify-content:center;top:1398px}
.reviews{left:0;top:1475px;width:1200px;height:380px;background:var(--review-bg)}
.reviews-title{left:469px;top:1530px;width:262px;height:54px;font-size:30px;color:#4a4a4a;font-weight:700;letter-spacing:-.5px}
.review{width:400px;border-left:1px solid #d9d9d9;height:179px;top:1630px}
.review p{margin-left:25px;font-style:italic;font-size:13px;line-height:23px;color:var(--muted)}
.review q{quotes:none}
.review .avatar{position:absolute;left:25px;top:87px;width:76px;height:76px;border-radius:50%;background:radial-gradient(circle at 50% 40%,#c9a48a,#7b6a62);border:3px solid #fff}
.review .who{position:absolute;left:124px;top:108px;font-style:italic;font-size:12.5px;color:var(--ink)}
.review .stars{position:absolute;left:124px;top:131px;font-size:11px;letter-spacing:1px;color:var(--star)}
.stars .off{color:#bbb}
.footer{left:0;top:1855px;width:1200px;height:271px;background:var(--footer)}
.footer-logo{left:97px;top:1956px;font-size:30px;color:#fff}
.social{left:137px;top:2012px;display:flex;gap:8px}
.social i{width:20px;height:20px;border-radius:50%;background:#fff;display:block}
.f-head{font-family:"Roboto Condensed",sans-serif;font-size:18px;font-weight:400;color:#fff}
.contact-line{left:347px;display:flex;gap:17px;color:#fff;font-size:12px;line-height:20px;letter-spacing:.3px}
.contact-line svg{flex:none;margin-top:2px}
.links{left:674px;top:1948px;list-style:none}
.links li{font-size:11.5px;color:#fff;height:24px;line-height:24px}
.news-text{left:859px;top:1941px;width:230px;font-size:11px;line-height:19px;color:#fff}
.news-input{left:859px;top:1992px;width:241px;height:39px;background:#fff;font-size:11px;color:#555;padding:12px 13px}
.news-btn{left:859px;top:2047px;width:101px;height:39px;background:#111;color:#fff;font-size:12px;font-weight:600;display:flex;align-items:center;justify-content:center}
.bottombar{left:0;top:2126px;width:1200px;height:53px;background:var(--bottom);color:#ddd;font-size:12px;text-align:center;line-height:53px}
</style>
</head>
<body>

<svg width="0" height="0" style="position:absolute">
  <defs>
    <symbol id="bullet" viewBox="0 0 14 14"><circle cx="7" cy="7" r="6.5" fill="#1a64a6"/><path d="M5.7 4.3 8.4 7l-2.7 2.7" stroke="#fff" stroke-width="1.6" fill="none"/></symbol>
    <symbol id="bullet-line" viewBox="0 0 14 14"><circle cx="7" cy="7" r="6" fill="none" stroke="#333"/><path d="M5.8 4.5 8.3 7l-2.5 2.5" stroke="#333" stroke-width="1.2" fill="none"/></symbol>
  </defs>
</svg>

<div class="abs topbar">
  <span style="left:742px">LOGIN &amp; REGISTER</span>
  <span style="left:898px">MY ACCOUNT</span>
  <span style="left:1020px">ENGLISH &#8964;</span>
</div>

<header class="abs header">
  <div class="abs logo header-logo">TALBIX</div>
  <nav class="nav">
    <a class="active" style="left:633px">HOME</a>
    <a style="left:713px">ABOUT US</a>
    <a style="left:808px">OUR PRODUCTS</a>
    <a style="left:936px">REVIEWS</a>
    <a style="left:1024px">CONTACT US</a>
  </nav>
</header>

<section class="hero">
  <div class="abs framed hero-title">TALBIX KESTRA</div>
  <p class="abs hero-text">Sed ut perspiciatis unde omnis iste natus error sit voluptatem accusantium doloremque laudantium, totam rem</p>
  <ul class="abs specs hero-specs">
    <li><svg width="14" height="14"><use href="#bullet"/></svg>Tip size: 0.7mm</li>
    <li><svg width="14" height="14"><use href="#bullet"/></svg>5pcs pouch</li>
    <li><svg width="14" height="14"><use href="#bullet"/></svg>Available: <span class="swatch sw-blue"></span><span class="swatch sw-black"></span></li>
  </ul>
  <div class="abs dots"><i class="on"></i><i></i><i></i><i></i><i></i></div>
  <div class="abs pen-art" role="img" aria-label="Light blue Talbix Kestra pen writing a loop" style="left:726px;top:182px;width:233px;height:353px"></div>
</section>

<section class="welcome">
  <svg class="abs" style="left:99px;top:556px" width="1001" height="330" viewBox="0 0 1001 330" role="img" aria-label="Blue band over a soft wooden desk texture">
    <defs>
      <radialGradient id="bandShadow" cx="50%" cy="0%" r="60%"><stop offset="0" stop-color="#000" stop-opacity=".18"/><stop offset="1" stop-color="#000" stop-opacity="0"/></radialGradient>
    </defs>
    <ellipse cx="500" cy="301" rx="480" ry="28" fill="url(#bandShadow)"/>
    <polygon points="0,0 500,43 1001,0 1001,301 500,287 0,301" fill="var(--blue-band)"/>
  </svg>
  <h1 class="abs welcome-title">WELCOME TO TALBIX</h1>
  <p class="abs welcome-text">Lorem ipsum dolor sit amet, consectetur adipiscing elit, sed do eiusmod tempor incididunt ut labore et dolore magna aliqua. Ut enim ad minim veniam, quis nostrud exercitation ullamco laboris nisi ut aliquip ex ea commodo consequat. Duis aute irure dolor in reprehenderit in voluptate velit esse cillum dolore eu fugiat nulla pariatur. Excepteur sint occaecat cupidatat non proident, sunt in culpa qui officia deserunt mollit</p>
</section>

<section class="products">
  <h2 class="abs framed products-title">OUR PRODUCTS</h2>

  <article class="abs product" style="left:97px;top:1012px">
    <h3><b>TALBIX</b>VELORA</h3>
    <ul class="specs">
      <li><svg width="12" height="12"><use href="#bullet-line"/></svg>Tip size: 0.7mm</li>
      <li><svg width="12" height="12"><use href="#bullet-line"/></svg>5pcs pouch</li>
      <li><svg width="12" height="12"><use href="#bullet-line"/></svg>Available: <span class="swatch sw-blue"></span><span class="swatch sw-black"></span><span class="swatch sw-red"></span></li>
    </ul>
  </article>
  <div class="abs pen-art pen-purple" role="img" aria-label="Clear Talbix Velora pen with purple cap" style="left:196px;top:1132px;width:108px;height:228px"></div>

  <article class="abs product" style="left:372px;top:1012px">
    <h3><b>TALBIX</b>LUMINA</h3>
    <ul class="specs">
      <li><svg width="12" height="12"><use href="#bullet-line"/></svg>Tip size: 0.7mm</li>
      <li><svg width="12" height="12"><use href="#bullet-line"/></svg>5pcs pouch</li>
      <li><svg width="12" height="12"><use href="#bullet-line"/></svg>Available: <span class="swatch sw-blue"></span><span class="swatch sw-black"></span><span class="swatch sw-red"></span></li>
    </ul>
  </article>
  <div class="abs pen-art pen-purple" role="img" aria-label="Clear Talbix Lumina pen with purple cap" style="left:472px;top:1132px;width:108px;height:228px"></div>

  <article class="abs product" style="left:641px;top:1012px">
    <h3><b>TALBIX</b>KESTRA</h3>
    <ul class="specs">
      <li><svg width="12" height="12"><use href="#bullet-line"/></svg>Tip size: 0.7mm</li>
      <li><svg width="12" height="12"><use href="#bullet-line"/></svg>5pcs pouch</li>
      <li><svg width="12" height="12"><use href="#bullet-line"/></svg>Available: <span class="swatch sw-blue"></span><span class="swatch sw-black"></span></li>
    </ul>
  </article>
  <div class="abs pen-art" role="img" aria-label="Light blue Talbix Kestra pen" style="left:741px;top:1132px;width:102px;height:228px"></div>

  <article class="abs product" style="left:896px;top:1012px">
    <h3><b>TALBIX</b>ORBO</h3>
    <ul class="specs">
      <li><svg width="12" height="12"><use href="#bullet-line"/></svg>Tip size: 0.7mm</li>
      <li><svg width="12" height="12"><use href="#bullet-line"/></svg>5pcs pouch</li>
      <li><svg width="12" height="12"><use href="#bullet-line"/></svg>Available: <span class="swatch sw-blue"></span><span class="swatch sw-black"></span></li>
    </ul>
  </article>
  <div class="abs pen-art pen-purple" role="img" aria-label="Clear Talbix Orbo pen with purple cap" style="left:990px;top:1132px;width:110px;height:228px"></div>

  <div class="abs arrow" style="left:569px"><svg width="10" height="10"><path d="M6.5 1.5 3 5l3.5 3.5" stroke="#333" fill="none" stroke-width="1.3"/></svg></div>
  <div class="abs arrow" style="left:603px"><svg width="10" height="10"><path d="M3.5 1.5 7 5 3.5 8.5" stroke="#1a64a6" fill="none" stroke-width="1.3"/></svg></div>
</section>

<section class="abs reviews"></section>
<h2 class="abs framed reviews-title">Customer Reviews</h2>
<div class="abs review" style="left:138px">
  <p><q>&#8220; Sed ut perspiciatis unde omnis iste natus error sit voluptatem accusantium doloremque laudantium, totam rem aperiam, eaque ipsa quae ab illo inventore veritatis</q></p>
  <div class="avatar" role="img" aria-label="Customer portrait"></div>
  <div class="who">JOHN DOE - TALBIX PENS</div>
  <div class="stars">&#9733;&#9733;&#9733;<span class="off">&#9734;&#9734;</span></div>
</div>
<div class="abs review" style="left:661px">
  <p><q>&#8220; Sed ut perspiciatis unde omnis iste natus error sit voluptatem accusantium doloremque laudantium, totam rem aperiam, eaque ipsa quae ab illo inventore veritatis</q></p>
  <div class="avatar" role="img" aria-label="Customer portrait"></div>
  <div class="who">JOHN DOE - TALBIX PENS</div>
  <div class="stars">&#9733;&#9733;&#9733;<span class="off">&#9734;&#9734;</span></div>
</div>

<footer>
  <div class="abs footer"></div>
  <div class="abs logo footer-logo">TALBIX</div>
  <div class="abs social"><i></i><i></i><i></i><i></i></div>

  <h4 class="abs f-head" style="left:347px;top:1906px">CONTACT US</h4>
  <div class="abs contact-line" style="top:1953px">
    <svg width="16" height="20" viewBox="0 0 16 20"><path d="M8 1a6 6 0 0 0-6 6c0 4.5 6 11 6 11s6-6.5 6-11a6 6 0 0 0-6-6z" fill="none" stroke="#fff" stroke-width="1.3"/><circle cx="8" cy="7" r="2.2" fill="none" stroke="#fff" stroke-width="1.3"/></svg>
    <span>Talbix Pens<br>Harlow Bend, Western Australia,<br>6099.</span>
  </div>
  <div class="abs contact-line" style="top:2023px">
    <svg width="16" height="16" viewBox="0 0 16 16"><path d="M3 1.5l3 3-1.5 2a9 9 0 0 0 5 5l2-1.5 3 3-2 2C6 15 1 10 1 3.5z" fill="none" stroke="#fff" stroke-width="1.2"/></svg>
    <span>Phone: +61 0400 117 352</span>
  </div>
  <div class="abs contact-line" style="top:2056px">
    <svg width="16" height="14" viewBox="0 0 16 14"><rect x=".6" y="1.6" width="14.8" height="10.8" fill="none" stroke="#fff" stroke-width="1.2"/><path d="M1 2l7 6 7-6" fill="none" stroke="#fff" stroke-width="1.2"/></svg>
    <span>E-mail : info@talbixpens.example</span>
  </div>

  <h4 class="abs f-head" style="left:674px;top:1903px">QUICK LINKS</h4>
  <ul class="abs links">
    <li>TALBIX VELORA</li>
    <li>TALBIX LUMINA</li>
    <li>TALBIX KESTRA</li>
    <li>TALBIX ORBO</li>
    <li>TALBIX NIMBO</li>
    <li>CONTACT US</li>
  </ul>

  <h4 class="abs f-head" style="left:859px;top:1900px">JOIN OUR NEWSLETTER</h4>
  <p class="abs news-text">Excepteur sint occaecat cupidatat non proident, sunt in culpa qui</p>
  <div class="abs news-input">Enter Name</div>
  <div class="abs news-btn">SUBSCRIBE</div>

  <div class="abs bottombar">Copyright 2016 | All Rights Reserved -- Talbix Pens</div>
</footer>

</body>
</html>
```